Video Thumbnail Design for Jazz Piano YouTube channel

Hello, my name’s Marcus Fenwick. I run a jazz piano YouTube channel called ‘Keyhaven Lessons’ (www.vidstreamer.example/keyhavenlessons). It’s the most subscribed to jazz piano YouTube channel with over 200,000 subscribers.

I need a designer to create an eye-catching thumbnail, to be used for my upcoming videos.

BRIEF:
For now, I’m asking for just one thumbnail design. I will choose a designer from this initial project, and I plan to commission additional designs from the same designer - so that my thumbnails all have a coherent look.

WHAT MAKES A GOOD THUMBNAIL:
Above all, your thumbnail design must be EYE-CATCHING and STAND OUT. Imagine scrolling through hundreds of YouTube videos - the video’s thumbnail artwork is one of the key aspects that gets someone to click and watch a video, so this is a VERY important aspect to getting views.

Your design can be innovative - surprise me. I want your design to JUMP OUT at me. For example, you could experiment with creating a 3D effect, or having elements popping out of the frame. A YouTube thumbnail doesn’t have to be square to the edges - you can add white around the edges to create an unusual jagged effect (when viewed in YouTube's search, which has a white background), and certain things could come out of the picture (see attached files for reference).

Remember, YouTube thumbnails are displayed very small - especially on desktop. It’s a good idea to design your thumbnail at this small size, rather than at full size on your computer screen. You'll probably need to zoom in closer to my face and enlarge the text more than you normally would if you were creating a larger image.

Lots of contrast is needed in a tiny thumbnail. Blacks must be pitch black, whites must be white, color saturation - the thumbnail must contain a lot of energy in a small space.

A strong format for YouTube thumbnails is to have a FACE (my face) and TEXT (large white text, 3 - 5 words). You can use this if you like, or you can experiment with a different format. I’m completely open to your ideas.

BRAND LOOK & FEEL:
Here are some keywords that describe my brand:
- Calm
- Professional
- Sophisticated (jazz is a sophisticated style of music)
View my channel to see my visual style as a starting point: www.vidstreamer.example/keyhavenlessons

BRAND COLORS:
- Turquoise: Hex #00DBD7 (this is my main brand color and must be used in the thumbnail)
- Black
- White
- Red: #FC5B5B (I sometimes use this as a secondary color - you can use this in your design if you want, or not).

TEXT:
The font I use for my brand is ‘Lovelo’ (please use this font in your design - included in my attachment).
I like my text to be white against a black background.
For your design, you could use the text: 'SWEET CHORD VOICING' as sample text.

IMAGES:
I've attached several photos for you to work with - just choose one for your design. The backgrounds are not important to the Thumbnail - only me and the piano are needed - so it's up to you whether you black out the background, darken it, or leave it in. Feel free to zoom in, rotate at an angle, distort, etc.

SLANTS:
I like diagonal lines and slants - because they go well with the ‘jazz’ feel. This could include the text itself (at an angle instead of straight), or the picture (any images of me or the piano could be at an angle, rather than straight).

DIMENSIONS:
YouTube thumbnails must be 1280 pixels wide by 720 pixels tall. A ratio of 16:9 is ideal as it’s used most often in YouTube players and previews.

DELIVERABLES:
If your design is selected - I will need a Photoshop file delivered of the final design (this is so that I can edit the text myself to make it relevant to the video).

After that, I will commission further designs with you (these will be separate projects, each with its own payment). My end goal is to have 10 - 15 strong thumbnail designs - all from the same designer.

Thank you very much for your submission, I can't wait to see what you come up with!

Target Market(s)

My audience is 90% male, between 25 - 65 years old. I have viewers worldwide, but they mostly live in the US and Canada.

Font styles to use
Other font styles liked:
• Lovelo

Colors
31b7a3

Requirements
Must have
• Image and text (as described in the project description)
Nice to have
• Creative use of white edges to stand out on YouTube (against other traditional square looking thumbnails).
• See full description in the project description.

```html
<!DOCTYPE html>
<html lang="en">
<head>
<meta charset="utf-8">
<title>Sweet Chord Voicing – thumbnail concepts</title>
<link rel="stylesheet" href="https://fonts.googleapis.com/css2?family=Josefin+Sans:wght@700&family=Roboto:wght@400&display=swap">
<style>
  :root {
    --paper: #ffffff;
    --ink: #161314;
    --frame: #6b6b6b;
    --turquoise: #23b59c;
    --turquoise-dark: #12695c;
    --red: #e3232d;
    --white: #ffffff;
    --skin: #e8b49e;
    --shirt: #9fe3d8;
    --keys: #f1f1f1;
  }
  html, body {
    margin: 0;
    padding: 0;
    overflow: hidden;
    background: var(--paper);
  }
  .sheet {
    position: relative;
    width: 851px;
    height: 1200px;
    box-sizing: border-box;
    border: 1px solid var(--frame);
    background: var(--paper);
  }
  .sheet svg { display: block; }
  .variant-label {
    font-family: "Roboto", Arial, sans-serif;
    font-size: 50px;
    fill: #111;
  }
  .headline {
    font-family: "Josefin Sans", "Century Gothic", sans-serif;
    font-weight: 700;
    text-anchor: end;
    letter-spacing: 1px;
  }
  .headline .shadow-red { fill: var(--red); }
  .headline .shadow-teal { fill: var(--turquoise); }
  .headline .face { fill: var(--white); }
  .arrow { fill: var(--white); stroke: var(--red); stroke-width: 4; stroke-linejoin: miter; }
</style>
</head>
<body>
<div class="sheet">
<svg width="851" height="1200" viewBox="0 0 1064 1500" xmlns="http://www.w3.org/2000/svg">
  <defs>
    <linearGradient id="stripe-fade" x1="0" y1="0" x2="0" y2="1">
      <stop offset="0" stop-color="#ffffff"/>
      <stop offset="1" stop-color="#23b59c"/>
    </linearGradient>
    <linearGradient id="stripe-fade-b" x1="0" y1="0" x2="0" y2="1">
      <stop offset="0" stop-color="#9fd9cf"/>
      <stop offset="1" stop-color="#12695c"/>
    </linearGradient>
    <linearGradient id="photo-tones" x1="0" y1="0" x2="1" y2="0.4">
      <stop offset="0" stop-color="#e8b49e"/>
      <stop offset="0.3" stop-color="#9fe3d8"/>
      <stop offset="0.55" stop-color="#2a2a2a"/>
      <stop offset="1" stop-color="#e6e6e6"/>
    </linearGradient>
    <pattern id="stripes-a" width="18" height="10" patternUnits="userSpaceOnUse">
      <rect width="8" height="10" fill="url(#stripe-fade)"/>
    </pattern>
  </defs>

  <!-- Concept A -->
  <text class="variant-label" x="142" y="188">a</text>
  <g class="thumb thumb-a">
    <g class="stripes">
      <rect x="155" y="218" width="8" height="445" fill="url(#stripe-fade)" opacity="0.25"/>
      <rect x="175" y="218" width="8" height="445" fill="url(#stripe-fade)" opacity="0.35"/>
      <rect x="195" y="218" width="8" height="445" fill="url(#stripe-fade)" opacity="0.45"/>
      <rect x="215" y="218" width="8" height="445" fill="url(#stripe-fade)" opacity="0.55"/>
      <rect x="235" y="218" width="8" height="445" fill="url(#stripe-fade)" opacity="0.65"/>
      <rect x="255" y="218" width="8" height="445" fill="url(#stripe-fade)" opacity="0.75"/>
      <rect x="275" y="218" width="8" height="445" fill="url(#stripe-fade)" opacity="0.85"/>
      <rect x="295" y="218" width="8" height="445" fill="url(#stripe-fade)"/>
      <rect x="315" y="218" width="8" height="445" fill="url(#stripe-fade)"/>
    </g>
    <rect class="backdrop" x="330" y="218" width="615" height="445" fill="var(--ink)"/>
    <g class="backdrop-stripes" fill="var(--turquoise-dark)" opacity="0.55">
      <rect x="345" y="225" width="7" height="300"/>
      <rect x="370" y="240" width="7" height="290"/>
      <rect x="395" y="255" width="7" height="280"/>
      <rect x="420" y="270" width="7" height="270"/>
      <rect x="445" y="290" width="7" height="255"/>
      <rect x="470" y="305" width="7" height="245"/>
      <rect x="495" y="320" width="7" height="235"/>
      <rect x="520" y="340" width="7" height="220"/>
    </g>
    <path class="cutout-red" fill="var(--red)" d="M118,663 L130,615 L180,575 L200,525 L160,470 L150,390 L175,330 L230,298 L300,292 L330,315 L330,663 Z"/>
    <path class="cutout-teal" fill="var(--turquoise)" d="M135,663 L147,615 L195,575 L213,525 L175,470 L165,392 L190,335 L245,304 L310,300 L340,320 L340,663 Z"/>
    <path class="photo" role="img" aria-label="Photo of the pianist looking back over his shoulder while playing a black stage piano"
          fill="url(#photo-tones)"
          d="M150,663 L162,618 L212,580 L228,530 L195,475 L182,400 L205,345 L258,312 L320,308 L372,345 L395,415 L408,460 L470,440 L945,555 L945,663 Z"/>
    <g class="headline" font-size="82">
      <text class="shadow-red" x="886" y="302">SWEET</text>
      <text class="shadow-teal" x="893" y="302">SWEET</text>
      <text class="face" x="890" y="302">SWEET</text>
      <text class="shadow-red" x="886" y="387">CHORD</text>
      <text class="shadow-teal" x="893" y="387">CHORD</text>
      <text class="face" x="890" y="387">CHORD</text>
      <text class="shadow-red" x="886" y="470">VOICING</text>
      <text class="shadow-teal" x="893" y="470">VOICING</text>
      <text class="face" x="890" y="470">VOICING</text>
    </g>
    <polygon class="arrow" points="797,500 868,500 845,523 886,566 864,586 823,544 800,567"/>
  </g>

  <!-- Concept B -->
  <text class="variant-label" x="142" y="790">b</text>
  <g class="thumb thumb-b">
    <g class="stripes">
      <rect x="140" y="803" width="9" height="444" fill="url(#stripe-fade-b)"/>
      <rect x="162" y="803" width="9" height="444" fill="url(#stripe-fade-b)"/>
      <rect x="184" y="803" width="9" height="444" fill="url(#stripe-fade-b)"/>
      <rect x="206" y="803" width="9" height="444" fill="url(#stripe-fade-b)"/>
      <rect x="228" y="803" width="9" height="444" fill="url(#stripe-fade-b)"/>
      <rect x="250" y="803" width="9" height="444" fill="url(#stripe-fade-b)"/>
      <rect x="272" y="803" width="9" height="444" fill="url(#stripe-fade-b)"/>
      <rect x="294" y="803" width="9" height="444" fill="url(#stripe-fade-b)"/>
      <rect x="316" y="803" width="9" height="444" fill="url(#stripe-fade-b)"/>
      <rect x="338" y="803" width="9" height="444" fill="url(#stripe-fade-b)"/>
      <rect x="360" y="803" width="9" height="444" fill="url(#stripe-fade-b)"/>
      <rect x="382" y="803" width="9" height="444" fill="url(#stripe-fade-b)"/>
      <rect x="404" y="803" width="9" height="444" fill="url(#stripe-fade-b)"/>
    </g>
    <polygon class="accent-red" fill="var(--red)" points="640,1060 915,1060 905,1128 640,1128"/>
    <polygon class="title-frame" fill="var(--turquoise)" points="425,803 855,803 936,1070 450,1070"/>
    <polygon class="title-panel" fill="var(--ink)" points="438,813 843,813 914,1058 462,1058"/>
    <path class="cutout-red" fill="var(--red)" d="M140,1247 L142,1150 L185,1110 L180,1055 L158,990 L165,925 L205,875 L265,858 L330,870 L330,1247 Z"/>
    <path class="cutout-teal" fill="var(--turquoise)" d="M168,1247 L170,1150 L210,1112 L205,1055 L185,992 L192,930 L230,885 L285,868 L345,880 L345,1247 Z"/>
    <path class="photo" role="img" aria-label="Photo of the pianist smiling over his shoulder at a black stage piano, keyboard running off to the right"
          fill="url(#photo-tones)"
          d="M200,1247 L202,1150 L240,1115 L235,1058 L215,1000 L222,940 L255,895 L305,880 L365,900 L405,950 L420,1010 L455,1030 L935,1130 L935,1247 Z"/>
    <g class="headline" font-size="74">
      <text class="shadow-red" x="821" y="882">SWEET</text>
      <text class="shadow-teal" x="828" y="882">SWEET</text>
      <text class="face" x="825" y="882">SWEET</text>
      <text class="shadow-red" x="821" y="953">CHORD</text>
      <text class="shadow-teal" x="828" y="953">CHORD</text>
      <text class="face" x="825" y="953">CHORD</text>
      <text class="shadow-red" x="821" y="1023">VOICING</text>
      <text class="shadow-teal" x="828" y="1023">VOICING</text>
      <text class="face" x="825" y="1023">VOICING</text>
    </g>
    <polygon class="arrow" points="545,880 545,950 523,928 483,968 463,948 503,908 481,880"/>
  </g>
</svg>
</div>
</body>
</html>
```